Sri Lankan Cricket Tour For Girls Aged 14-18 in July 2018

We need a flyer to promote a cricket tour of Sri Lanka in July 2018 for girls aged 14-18.
We want the flyer to call for "expressions of interest".
We would like the Sri Lankan Flag also images of cricket ball and beaches and palm trees etc.
Mention Level 3 Coaches with International experience.
Target market is parents of girls aged 14 to 18 and girls aged 14 to 18

Target Market(s)

Parents of girls aged 14 to 18 and girls aged 14 to 18

Industry/Entity Type

Travel

Font styles to use
Serif
Sans Serif

Colors
0355a3
ec1f27
fbed22

Requirements
Must have
• Sri Lankan Flag, Halvey Athletics Logo, email address boyd@halveyathletics.com.au.
• - 10 Day Tour
• - Play on First Class Grounds
• - Level 3 Coaches With International Experience
• - For More Information Contact Boyd boyd@halveyathletics.com.au
Nice to have
• Picture of girls playing cricket, sun and beach
Should not have
• Cartoon type images
• Photo's of actual cricketers

```html
<!DOCTYPE html>
<html lang="en">
<head>
<meta charset="utf-8">
<title>Halvey Athletics – Cricket Tour of Sri Lanka</title>
<link rel="stylesheet" href="https://fonts.googleapis.com/css2?family=Days+One&family=Montserrat:wght@700;800;900&display=swap">
<style>
  :root {
    --brand-blue: #0355a3;
    --brand-red: #ec1f27;
    --brand-yellow: #fbed22;
    --ribbon-dark: #9e1118;
    --night: #161616;
    --ink: #111111;
    --white: #ffffff;
  }
  html, body {
    margin: 0;
    padding: 0;
    width: 927px;
    height: 1200px;
    overflow: hidden;
    background: var(--white);
  }
  .flyer { display: block; width: 927px; height: 1200px; }
  .brand-name { font-family: "Days One", sans-serif; font-size: 40px; fill: var(--brand-red); letter-spacing: 2px; }
  .ribbon-text { font-family: "Days One", sans-serif; fill: var(--white); }
  .headline { font-size: 46px; letter-spacing: 1px; }
  .tour-line { font-size: 29px; }
  .date { font-size: 54px; }
  .date-shadow { font-family: "Days One", sans-serif; font-size: 54px; fill: var(--brand-blue); }
  .feature { font-family: "Montserrat", sans-serif; font-weight: 900; font-size: 37px; fill: var(--ink); letter-spacing: 1px; }
  .bullet { fill: var(--brand-red); }
  .contact { font-family: "Montserrat", sans-serif; font-weight: 800; fill: var(--white); letter-spacing: 1px; }
  .contact-label { font-size: 25px; }
  .contact-email { font-size: 31px; }
</style>
</head>
<body>
<svg class="flyer" viewBox="0 0 1000 1294" xmlns="http://www.w3.org/2000/svg">
  <defs>
    <linearGradient id="sceneTone" x1="0" y1="0" x2="0" y2="1">
      <stop offset="0" stop-color="#6fbde8"/>
      <stop offset="0.35" stop-color="#cfe9f7"/>
      <stop offset="0.43" stop-color="#4fc8d2"/>
      <stop offset="0.68" stop-color="#8fd8d6"/>
      <stop offset="0.76" stop-color="#e6dccb"/>
      <stop offset="1" stop-color="#cdbfa6"/>
    </linearGradient>
    <linearGradient id="flagTone" x1="0" y1="0" x2="1" y2="0">
      <stop offset="0" stop-color="#8c1d40"/>
      <stop offset="0.6" stop-color="#8c1d40"/>
      <stop offset="0.8" stop-color="#f7941d"/>
      <stop offset="1" stop-color="#1f9a4a"/>
    </linearGradient>
    <radialGradient id="ballTone" cx="0.4" cy="0.35" r="0.7">
      <stop offset="0" stop-color="#ffffff"/>
      <stop offset="1" stop-color="#c9cdd2"/>
    </radialGradient>
    <linearGradient id="nightTone" x1="0" y1="0" x2="0" y2="1">
      <stop offset="0" stop-color="#0d0d0d"/>
      <stop offset="1" stop-color="#262626"/>
    </linearGradient>
    <linearGradient id="photoTone" x1="0" y1="0" x2="0" y2="1">
      <stop offset="0" stop-color="#c8d7e4"/>
      <stop offset="1" stop-color="#5f9a4a"/>
    </linearGradient>
  </defs>

  <!-- beach scene -->
  <rect class="scene" x="0" y="230" width="1000" height="1064" fill="url(#sceneTone)" role="img" aria-label="Tropical beach with palm tree, turquoise sea and sunny sky"/>

  <!-- header -->
  <g class="header">
    <polygon points="0,0 1000,0 1000,250 0,340" fill="url(#nightTone)"/>
    <polygon points="0,340 1000,250 1000,258 0,348" fill="var(--brand-blue)"/>
    <polygon points="0,348 1000,258 1000,264 0,354" fill="var(--brand-red)"/>
    <circle cx="295" cy="130" r="70" fill="none" stroke="var(--brand-blue)" stroke-width="12"/>
    <text class="brand-name" x="80" y="262">HALVEY ATHLETICS</text>
  </g>

  <!-- flag -->
  <g transform="rotate(-17 780 215)">
    <rect x="585" y="95" width="390" height="245" fill="url(#flagTone)" stroke="var(--brand-yellow)" stroke-width="12" role="img" aria-label="Flag of Sri Lanka"/>
  </g>

  <!-- cricket ball -->
  <circle cx="510" cy="505" r="118" fill="url(#ballTone)" role="img" aria-label="White cricket ball"/>

  <!-- headline ribbons -->
  <g transform="rotate(-14 300 560)">
    <polygon points="90,540 470,540 470,560 90,560" fill="var(--brand-blue)"/>
    <polygon points="100,460 505,460 490,500 505,540 100,540 115,500" fill="var(--brand-red)"/>
    <text class="ribbon-text headline" x="120" y="518">EXPRESSIONS</text>
    <polygon points="80,590 460,590 445,630 460,670 80,670 95,630" fill="var(--brand-red)"/>
    <text class="ribbon-text headline" x="110" y="648">OF INTEREST</text>
  </g>

  <!-- tour band -->
  <g transform="rotate(-13 500 740)">
    <polygon points="-60,700 640,700 640,800 -60,800" fill="var(--brand-red)"/>
    <polygon points="640,700 1080,670 1080,770 640,800" fill="var(--ribbon-dark)"/>
    <text class="ribbon-text tour-line" x="40" y="742">Cricket Tour Of Sri Lanka</text>
    <text class="ribbon-text tour-line" x="75" y="782">For Girls  Aged 14 -18</text>
    <text class="date-shadow" x="683" y="764">July 2018</text>
    <text class="ribbon-text date" x="679" y="760">July 2018</text>
  </g>

  <!-- photos -->
  <g transform="translate(66,880) rotate(-8)">
    <rect width="265" height="170" fill="var(--brand-red)"/>
    <rect x="8" y="8" width="249" height="154" fill="url(#photoTone)" role="img" aria-label="Girls playing cricket on a field"/>
  </g>
  <g transform="translate(98,1045) rotate(-8)">
    <rect width="265" height="160" fill="var(--brand-red)"/>
    <rect x="8" y="8" width="249" height="144" fill="url(#photoTone)" role="img" aria-label="Girl batting in front of the wickets"/>
  </g>

  <!-- features -->
  <g transform="translate(405,952) rotate(-13)">
    <circle class="bullet" cx="-20" cy="-12" r="10"/>
    <text class="feature" x="0" y="0">FIRST CLASS GROUNDS</text>
    <circle class="bullet" cx="-20" cy="34" r="10"/>
    <text class="feature" x="0" y="46">10 DAY TOUR</text>
    <circle class="bullet" cx="-20" cy="80" r="10"/>
    <text class="feature" x="0" y="92">LEVEL 3 COACHES</text>
    <text class="feature" x="0" y="138">WITH INTERNATIONAL</text>
    <text class="feature" x="0" y="184">EXPERIENCE</text>
  </g>

  <!-- footer -->
  <g class="footer">
    <polygon points="0,1258 1000,1054 1000,1064 0,1268" fill="var(--brand-yellow)"/>
    <polygon points="0,1268 1000,1064 1000,1070 0,1274" fill="var(--brand-red)"/>
    <polygon points="0,1274 1000,1070 1000,1294 0,1294" fill="var(--brand-blue)"/>
    <text class="contact contact-label" x="958" y="1172" text-anchor="end">FOR MORE</text>
    <text class="contact contact-label" x="958" y="1208" text-anchor="end">INFORMATION CONTACT BOYD</text>
    <text class="contact contact-email" x="958" y="1246" text-anchor="end">BOYD@HALVEYATHLETICS.COM.AU</text>
  </g>
</svg>
</body>
</html>
```